Verdalo sage- referral cards for new customers

Hey,

I would like 1 set of business cards with the following details:

10% off any sales / coupon code
Our phone number: 5302749186
Menu :Verdalosage.example (for the menu)
A line left blank to hand write an activation code: either on top or just on one side

Include the Verdalo Sage logo ( your choice of black or white logo)
This card is to drive orders for people to order a cannabis order with Verdalo Sage. Please make the logo a large part of the card on both sides.

Target Market(s)

People who consume cannabis 21 and up

Industry/Entity Type

Business

Contact Information for Business Card

This business card will be given to customers so they can then give it to other customers and generate referalls. We need this card to be elegant, impressionable, professional, and something worth keeping and passing to friends.

Font styles to use
Decorative
Script

Colors
33a6d7
85acd3
3176b5
0455a3
0592cd
85cae6
cee9f5
eaf1f7
757575

Requirements
Must have
• Our website
• Phone Number
• The 10% off an order
• Spot for activation code
Nice to have
• Eye catching design
• Look classy
• Textured feel or textured look
Should not have
• Do not look super cannabis heady
• Do not look attractive to children

```html
<!DOCTYPE html>
<html lang="en">
<head>
<meta charset="utf-8">
<title>Verdalo Sage – Referral Card</title>
<link rel="stylesheet" href="https://fonts.googleapis.com/css2?family=Poiret+One&family=Anton&family=Oswald:wght@500;700&display=swap">
<style>
  :root {
    --backdrop: #2e2e2e;
    --card-top: #c6e9ee;
    --card-bottom: #9fc7cd;
    --ink: #161616;
    --code-field: #c9cdce;
    --art-olive: #5d6a2a;
    --art-blue: #7fb4c4;
    --art-dark: #2e2a33;
    --art-gold: #d2a21c;
  }
  * { box-sizing: border-box; margin: 0; padding: 0; }
  html, body {
    width: 1200px; height: 900px; overflow: hidden;
    background: var(--backdrop);
  }
  .sheet {
    position: relative; width: 1200px; height: 900px;
    display: flex; justify-content: center; align-items: center; gap: 60px;
  }
  .card {
    position: relative; width: 360px; height: 600px; overflow: hidden;
    background: linear-gradient(180deg, var(--card-top), var(--card-bottom));
    color: var(--ink);
    box-shadow: 0 10px 30px rgba(0,0,0,.45);
  }

  /* front */
  .front-art {
    position: absolute; left: 80px; top: 70px; width: 420px; height: 470px;
  }
  .front-name {
    position: absolute; left: 28px; bottom: 40px;
    transform-origin: left bottom; transform: rotate(-90deg) translateY(100%);
    font-family: "Poiret One", sans-serif; font-size: 58px; letter-spacing: 3px;
    white-space: nowrap; line-height: 1;
  }

  /* back */
  .back {
    display: flex; flex-direction: column; align-items: center;
    padding-top: 34px;
  }
  .back-art { width: 190px; height: 160px; }
  .back-name {
    margin-top: 14px;
    font-family: "Poiret One", sans-serif; font-size: 34px; letter-spacing: 2px;
  }
  .offer {
    display: flex; align-items: flex-end; margin-top: 18px; line-height: 0.85;
  }
  .offer-value { font-family: "Anton", sans-serif; font-size: 104px; }
  .offer-detail {
    display: flex; flex-direction: column; margin-left: 6px; padding-bottom: 8px;
  }
  .offer-off { font-family: "Anton", sans-serif; font-size: 58px; }
  .offer-scope { font-family: "Oswald", sans-serif; font-weight: 700; font-size: 24px; }
  .code-row {
    width: 300px; margin-top: 14px; display: flex; align-items: flex-end; gap: 10px;
  }
  .code-label {
    font-family: "Oswald", sans-serif; font-weight: 500; font-size: 13px;
    letter-spacing: .5px; white-space: nowrap;
  }
  .code-field {
    background: var(--code-field); border-radius: 8px;
  }
  .code-field.short { flex: 1; height: 34px; }
  .code-field.wide { width: 300px; height: 42px; margin-top: 12px; }
  .phone {
    margin-top: 14px;
    font-family: "Oswald", sans-serif; font-weight: 700; font-size: 36px; letter-spacing: 1px;
  }
  .website {
    font-family: "Oswald", sans-serif; font-weight: 700; font-size: 18px; letter-spacing: 1px;
  }
</style>
</head>
<body>
<main class="sheet">
  <section class="card front">
    <svg class="front-art" viewBox="0 0 420 470" role="img" aria-label="Brand illustration: seated sage figure framed by green leaves on a coloured mandala disc">
      <defs>
        <radialGradient id="frontGlow" cx="50%" cy="50%" r="50%">
          <stop offset="0%" stop-color="var(--art-blue)"/>
          <stop offset="70%" stop-color="var(--art-olive)"/>
          <stop offset="100%" stop-color="var(--art-dark)"/>
        </radialGradient>
      </defs>
      <circle cx="210" cy="235" r="220" fill="url(#frontGlow)"/>
    </svg>
    <div class="front-name">Verdalo Sage</div>
  </section>

  <section class="card back">
    <svg class="back-art" viewBox="0 0 190 160" role="img" aria-label="Small brand illustration: sage figure on a leaf-framed mandala">
      <defs>
        <radialGradient id="backGlow" cx="50%" cy="50%" r="50%">
          <stop offset="0%" stop-color="var(--art-blue)"/>
          <stop offset="70%" stop-color="var(--art-olive)"/>
          <stop offset="100%" stop-color="var(--art-dark)"/>
        </radialGradient>
      </defs>
      <circle cx="95" cy="80" r="78" fill="url(#backGlow)"/>
    </svg>
    <div class="back-name">Verdalo Sage</div>
    <div class="offer">
      <span class="offer-value">10%</span>
      <span class="offer-detail">
        <span class="offer-off">OFF</span>
        <span class="offer-scope">ANY SALES</span>
      </span>
    </div>
    <div class="code-row">
      <span class="code-label">ACTIVATION CODE</span>
      <span class="code-field short"></span>
    </div>
    <div class="code-field wide"></div>
    <div class="phone">5 302 749 186</div>
    <div class="website">VERDALOSAGE.EXAMPLE</div>
  </section>
</main>
</body>
</html>
```